Corvane Solutions Website

Corvane Solutions (CS) provide Analytics & Enterprise Performance Management (EPM) advisory & consultancy services. We are passionate about data and making a difference for our clients by working in partnership with them, helping them on their journey to becoming an Corvane Solution. We deliver insights which give our clients a competitive edge and a much deeper understanding of their organisation.

We need a website which shows who we are, what we do and how we do it.

www.corvane-solutions.com is our very basic website at the moment. We want to completely revamp it with a corporate look

```html
<!DOCTYPE html>
<html lang="en">
<head>
<meta charset="utf-8">
<title>Corvane Solutions — Data Analytics &amp; EPM Consulting</title>
<link href="https://fonts.googleapis.com/css2?family=Poppins:wght@400;500;600;700&family=Lexend:wght@500;600;700&display=swap" rel="stylesheet">
<style>
:root{
  --navy:#2b5170;
  --navy-dark:#24465f;
  --orange:#e0845a;
  --orange-dark:#d9703f;
  --ink:#2a2a2a;
  --muted:#555;
  --grey-band:#eef1f5;
  --card:#ffffff;
  --hero-a:#2f6aa3;
  --hero-b:#6fa9d8;
  --footer:#0c0c0c;
}
*{box-sizing:border-box;margin:0;padding:0}
html,body{width:1200px;height:4013px;overflow:hidden}
body{position:relative;font-family:"Poppins",sans-serif;color:var(--ink);background:#fff}
.abs{position:absolute}
.heading{font-family:"Lexend",sans-serif;font-weight:600;color:var(--navy)}
.eyebrow{font-size:13px;font-weight:600;color:var(--orange);letter-spacing:.3px;text-transform:uppercase}
.rule{width:52px;height:2px;background:#c9c9c9}
.btn{background:var(--orange);color:#fff;border-radius:4px;font-size:11px;font-weight:500;display:flex;align-items:center;justify-content:center}
.btn-pill{background:var(--orange);color:#fff;border-radius:22px;font-size:14px;font-weight:500;display:flex;align-items:center;justify-content:center;box-shadow:0 4px 12px rgba(0,0,0,.15)}

/* header */
.site-header{top:0;left:0;width:1200px;height:75px;background:rgba(255,255,255,.12);z-index:3}
.brand{left:160px;top:14px;display:flex;align-items:center;gap:10px;color:#fff}
.brand-dot{width:44px;height:44px;border-radius:50%;border:4px solid #fff}
.brand-name{font-size:16px;font-weight:600;line-height:19px;letter-spacing:.4px}
.nav{left:608px;top:28px;display:flex;gap:28px;font-size:12.5px;color:#fff}
.nav .active{color:var(--orange)}
.nav-btn{left:948px;top:21px;width:96px;height:32px;font-size:12.5px}

/* hero */
.hero{top:0;left:0;width:1200px;height:600px;background:linear-gradient(100deg,var(--hero-a) 0%,#4b88c2 45%,var(--hero-b) 100%)}
.hero-photo{top:0;left:0;width:560px;height:600px;background:linear-gradient(160deg,#1f4a72 0%,#5c88ad 55%,#b9cde0 100%);opacity:.9}
.slides{left:82px;top:198px;color:#fff;font-size:12px;font-weight:600;line-height:37px}
.slides .on{color:var(--orange);border:1.5px solid var(--orange);border-radius:50%;width:26px;height:26px;display:flex;align-items:center;justify-content:center;margin-left:-6px;line-height:1}
.hero-bar{left:600px;top:190px;width:6px;height:140px;background:var(--orange)}
.hero-title{left:632px;top:172px;font-family:"Lexend",sans-serif;font-weight:600;font-size:72px;line-height:88px;color:#fff}
.hero-sub{left:602px;top:364px;font-size:17px;color:#fff;letter-spacing:.6px}
.hero-btn{left:602px;top:412px;width:126px;height:38px}
.wave{left:0;top:500px}

/* services */
.svc-eyebrow{top:666px;left:0;width:1200px;text-align:center}
.svc-title{top:688px;left:0;width:1200px;text-align:center;font-size:34px}
.svc-rule{top:744px;left:574px}
.svc-card{top:785px;width:270px;height:300px;background:var(--card);box-shadow:0 6px 24px rgba(40,60,90,.09);border-radius:4px;text-align:center;padding-top:25px}
.icon-ring{width:96px;height:96px;border-radius:50%;margin:0 auto;background:#fff;box-shadow:0 4px 14px rgba(0,0,0,.12);border:2px solid #e6e9ee;display:flex;align-items:center;justify-content:center}
.icon-ring.filled{background:var(--navy);border-color:#5a7f9c}
.svc-card h3{font-size:16px;font-weight:600;margin-top:18px;color:var(--ink)}
.svc-card p{font-size:12px;color:var(--muted);line-height:20px;margin:14px 24px 0}

/* about */
.about-bg{left:0;top:1105px}
.about-photo{left:162px;top:1165px;width:444px;height:468px;background:linear-gradient(120deg,#e9eef3 0%,#cdd8e3 55%,#3a4f6b 100%)}
.about-monitor{left:66px;top:1200px;width:246px;height:250px;background:linear-gradient(180deg,#dce4ee,#b7c4d3);border-radius:6px}
.about-eyebrow{left:645px;top:1192px}
.about-title{left:645px;top:1210px;font-size:36px;line-height:38px}
.about-rule{left:645px;top:1318px}
.about-lead{left:645px;top:1355px;width:400px;font-size:12px;font-weight:600;line-height:20px;color:#222}
.about-text{left:645px;top:1450px;width:400px;font-size:12px;line-height:20px;color:var(--muted)}
.about-btn{left:645px;top:1575px;width:106px;height:33px}

/* process */
.process-bg{left:0;top:1700px}
.proc-eyebrow{left:160px;top:1866px}
.proc-title{left:160px;top:1885px;font-size:32px}
.proc-rule{left:160px;top:1948px}
.proc-lead{left:160px;top:1985px;width:390px;font-size:12px;font-weight:600;line-height:20px;color:#222}
.proc-list{left:160px;top:2080px;list-style:none;font-size:12px;color:#333}
.proc-list li{display:flex;align-items:center;gap:10px;height:33.5px}
.proc-btn{left:162px;top:2205px;width:106px;height:33px}
.proc-card{width:208px;height:208px;background:#fff;box-shadow:0 6px 22px rgba(40,60,90,.09);border-radius:4px;text-align:center;padding-top:34px}
.proc-card .icon-ring{width:92px;height:92px}
.proc-card span{display:block;margin-top:20px;font-size:14px;font-weight:500;color:var(--navy)}

/* clients */
.cli-eyebrow{top:2434px;left:0;width:1200px;text-align:center}
.cli-title{top:2452px;left:0;width:1200px;text-align:center;font-size:34px}
.cli-box{top:2550px;width:163px;height:77px;background:#fff;box-shadow:0 4px 16px rgba(0,0,0,.08);display:flex;align-items:center;justify-content:center;gap:8px;font-size:24px;font-weight:600;color:#222}
.cli-box.active{background:var(--orange);color:#fff}
.cli-mark{width:14px;height:14px;border-radius:50%;background:currentColor}
.cli-arrow{top:2570px;width:36px;height:36px;border-radius:50%;border:1.5px solid #bbb;display:flex;align-items:center;justify-content:center;color:#777;font-size:14px;background:#fff}

/* contact form */
.form-band{left:0;top:2930px;width:1200px;height:460px;background:var(--grey-band)}
.form-card{left:232px;top:2712px;width:736px;height:528px;background:#fff;box-shadow:0 8px 30px rgba(0,0,0,.08)}
.form-title{left:0;top:68px;width:736px;text-align:center;font-size:28px;line-height:38px;font-weight:600;color:#2d2d2d;letter-spacing:.4px}
.field{border:1px solid #d7d7d7;font-size:12px;color:#555;padding:10px 15px}
.submit{left:311px;top:414px;width:113px;height:35px;font-size:13px}
.fold{right:0;bottom:0}

/* cta */
.cta{left:0;top:3370px;width:1200px;height:430px;background:var(--navy)}
.cta-photo{left:820px;top:3310px;width:380px;height:460px;background:linear-gradient(180deg,#d9b8a2 0%,#3a5a8f 40%,#1f3b6e 100%);border-radius:200px 200px 0 0}
.cta-title{left:163px;top:3440px;font-family:"Lexend",sans-serif;font-size:40px;line-height:48px;font-weight:500;color:#fff}
.cta-line{left:163px;display:flex;align-items:center;gap:10px;color:#fff;font-size:16px;font-weight:500}
.cta-line i{width:1px;height:18px;background:rgba(255,255,255,.6);display:block}
.cta-rule{left:163px;top:3601px;width:393px;border-top:1px dashed rgba(255,255,255,.45)}
.cta-btn{left:163px;top:3670px;width:133px;height:40px}
.cta-curve{left:0;top:3700px}

/* footer */
.footer{left:0;top:3792px;width:1200px;height:221px;background:var(--footer);color:#fff}
.f-item{display:flex;align-items:center;gap:14px;font-size:12px;line-height:17px}
.f-icon{width:40px;height:40px;border-radius:50%;border:2px solid #fff;display:flex;align-items:center;justify-content:center;flex:none}
.f-sep{width:1px;height:36px;background:#444}
.f-brand{left:838px;top:75px;display:flex;align-items:center;gap:14px;font-size:18px;font-weight:600;line-height:21px;letter-spacing:.4px}
.f-brand .dot{width:52px;height:52px;border-radius:50%;border:5px solid #fff}
.copy{left:163px;top:180px;font-size:11px;color:#ccc}
.social{top:174px;width:28px;height:28px;border-radius:50%;background:#444}
</style>
</head>
<body>

<!-- HERO -->
<section class="abs hero" role="img" aria-label="Hero photograph: two business colleagues reviewing a tablet on a blue background"></section>
<div class="abs hero-photo" role="img" aria-label="Photo of a businessman and businesswoman looking at a tablet"></div>

<header class="abs site-header">
  <div class="abs brand"><span class="brand-dot"></span><span class="brand-name">CORVANE<br>SOLUTIONS</span></div>
  <nav class="abs nav"><span class="active">Home</span><span>Services</span><span>About Us</span><span>What We Do!</span></nav>
  <div class="abs btn-pill nav-btn">Contact Us</div>
</header>

<div class="abs slides"><div>01</div><div class="on">02</div><div>03</div><div>04</div></div>
<div class="abs hero-bar"></div>
<h1 class="abs hero-title">Corvane<br>Solutions</h1>
<p class="abs hero-sub">DATA ANALYTICS &amp; EPM CONSULTING SERVICES</p>
<div class="abs btn-pill hero-btn">Contact Us</div>

<svg class="abs wave" width="1200" height="110" viewBox="0 0 1200 110">
  <path d="M0 80 C200 50 380 40 520 60 C600 72 640 72 700 62 C880 30 1050 20 1200 40 L1200 110 L0 110Z" fill="#fff"/>
  <circle cx="600" cy="48" r="26" fill="#fff"/>
  <rect x="593" y="36" width="14" height="22" rx="7" fill="none" stroke="#333" stroke-width="1.6"/>
  <line x1="600" y1="41" x2="600" y2="46" stroke="#333" stroke-width="1.6"/>
  <path d="M596 62 L600 66 L604 62" fill="none" stroke="#333" stroke-width="1.4"/>
</svg>

<!-- SERVICES -->
<p class="abs eyebrow svc-eyebrow">Services</p>
<h2 class="abs heading svc-title">Best Solution For You</h2>
<div class="abs rule svc-rule"></div>

<article class="abs svc-card" style="left:162px">
  <div class="icon-ring"><svg width="40" height="40" viewBox="0 0 40 40" fill="none" stroke="#2b5170" stroke-width="1.6"><circle cx="20" cy="11" r="5"/><path d="M11 27c0-6 4-9 9-9s9 3 9 9"/><rect x="8" y="27" width="24" height="4"/><path d="M14 31v6M26 31v6"/></svg></div>
  <h3>Advise &amp; Architect</h3>
  <p>Helping our customers understand the art of the possible and safeguarding their investments by overseeing implementation.</p>
</article>
<article class="abs svc-card" style="left:466px">
  <div class="icon-ring filled"><svg width="40" height="40" viewBox="0 0 40 40" fill="none" stroke="#fff" stroke-width="1.6"><rect x="6" y="9" width="28" height="20" rx="2"/><circle cx="20" cy="19" r="5"/><path d="M14 34h12M20 29v5"/></svg></div>
  <h3>Design &amp; Implement</h3>
  <p>Working with the project management team, through each stage of the project, with clearly defined deliverables and well exercised plans to deliver them.</p>
</article>
<article class="abs svc-card" style="left:768px">
  <div class="icon-ring"><svg width="40" height="40" viewBox="0 0 40 40" fill="none" stroke="#2b5170" stroke-width="1.6"><rect x="6" y="8" width="28" height="24" rx="2"/><circle cx="20" cy="21" r="6"/><circle cx="20" cy="21" r="2"/><path d="M6 13h28"/></svg></div>
  <h3>Optimise &amp; Manage</h3>
  <p>Our Managed Services delivers proactive, on-demand support for EPM and Data Analytics environments.</p>
</article>

<!-- ABOUT -->
<svg class="abs about-bg" width="1200" height="620" viewBox="0 0 1200 620">
  <path d="M0 120 C300 30 700 20 1200 70 L1200 620 L0 620Z" fill="#f4f6f9"/>
  <path d="M0 620 L0 560 C400 470 800 470 1200 560 L1200 620Z" fill="#fff"/>
</svg>
<div class="abs about-photo" role="img" aria-label="Photo of a young businessman reading a report in an office"></div>
<div class="abs about-monitor" role="img" aria-label="Desktop monitor showing a bar chart"></div>
<p class="abs eyebrow about-eyebrow">About Corvane Solutions</p>
<h2 class="abs heading about-title">Always Company<br>Unique Solutions</h2>
<div class="abs rule about-rule"></div>
<p class="abs about-lead">CS are a Data Analytics &amp; EPM company, specialising in the implementation and support of Business Intelligence, EPM and Data Analytics business solutions, both in the Cloud and on-premise.</p>
<p class="abs about-text">Corvane Solutions is an exciting start-up in the Data Analytics and EPM space. Founded in 2019, CS specialise in the implementation and support of BI, EPM and Data Analytics business solutions, both in the Cloud and on-premise.</p>
<div class="abs btn about-btn">Read More</div>

<!-- PROCESS -->
<svg class="abs process-bg" width="1200" height="700" viewBox="0 0 1200 700">
  <path d="M0 110 C300 10 800 0 1200 80 L1200 620 C900 560 700 700 400 660 C250 640 100 600 0 620Z" fill="#f1f3f7"/>
</svg>
<p class="abs eyebrow proc-eyebrow">Our Process</p>
<h2 class="abs heading proc-title">How We Do It ?</h2>
<div class="abs rule proc-rule"></div>
<p class="abs proc-lead">Lorem ipsum dolor sit amet, consectetuer adipiscing elit, sed diam nonummy nibh euismod tincidunt ut laoreet dolore magna aliquam erat volutpat. Ut wisi enim ad minim veniam.</p>
<ul class="abs proc-list">
  <li><svg width="16" height="16" viewBox="0 0 16 16"><circle cx="8" cy="8" r="7" fill="#2b5170"/><path d="M4.5 8.2l2.3 2.2 4.5-4.6" stroke="#fff" stroke-width="1.6" fill="none"/></svg>Lorem ipsum dolor sit amet</li>
  <li><svg width="16" height="16" viewBox="0 0 16 16"><circle cx="8" cy="8" r="7" fill="#2b5170"/><path d="M4.5 8.2l2.3 2.2 4.5-4.6" stroke="#fff" stroke-width="1.6" fill="none"/></svg>Sed diam nonummy nibh euismod</li>
  <li><svg width="16" height="16" viewBox="0 0 16 16"><circle cx="8" cy="8" r="7" fill="#2b5170"/><path d="M4.5 8.2l2.3 2.2 4.5-4.6" stroke="#fff" stroke-width="1.6" fill="none"/></svg>Tincidunt ut laoreet dolore</li>
</ul>
<div class="abs btn proc-btn">Contact Us</div>

<div class="abs proc-card" style="left:592px;top:1810px">
  <div class="icon-ring"><svg width="36" height="36" viewBox="0 0 36 36" fill="none" stroke="#2b5170" stroke-width="1.5"><rect x="8" y="5" width="20" height="26" rx="2"/><path d="M12 11h12M12 16h12M12 21h12M12 26h8"/></svg></div><span>Lorem Ipsum</span></div>
<div class="abs proc-card" style="left:830px;top:1833px">
  <div class="icon-ring"><svg width="36" height="36" viewBox="0 0 36 36" fill="none" stroke="#2b5170" stroke-width="1.5"><path d="M18 8a7 7 0 0 0-4 12.7V24h8v-3.3A7 7 0 0 0 18 8z"/><path d="M15 28h6"/></svg></div><span>Onummy Nibh</span></div>
<div class="abs proc-card" style="left:592px;top:2050px">
  <div class="icon-ring"><svg width="36" height="36" viewBox="0 0 36 36" fill="none" stroke="#2b5170" stroke-width="1.5"><circle cx="18" cy="14" r="7"/><circle cx="18" cy="14" r="2.5"/><path d="M8 30c1-5 5-7 10-7s9 2 10 7"/></svg></div><span>Tincidunt Ut</span></div>
<div class="abs proc-card" style="left:830px;top:2073px">
  <div class="icon-ring"><svg width="36" height="36" viewBox="0 0 36 36" fill="none" stroke="#2b5170" stroke-width="1.5"><rect x="9" y="6" width="18" height="24" rx="2"/><path d="M13 13h10M13 18h10M13 23h6"/></svg></div><span>Nibh euismod</span></div>

<!-- CLIENTS -->
<p class="abs eyebrow cli-eyebrow">Clients</p>
<h2 class="abs heading cli-title">Our Customers</h2>
<div class="abs cli-arrow" style="left:88px">‹</div>
<div class="abs cli-box" style="left:162px"><span class="cli-mark"></span>Belmora</div>
<div class="abs cli-box active" style="left:340px"><span class="cli-mark"></span>Pinecrest</div>
<div class="abs cli-box" style="left:518px"><span class="cli-mark"></span>Lumora</div>
<div class="abs cli-box" style="left:696px"><span class="cli-mark"></span>Ostiva</div>
<div class="abs cli-box" style="left:874px"><span class="cli-mark"></span>Kestrel</div>
<div class="abs cli-arrow" style="left:1075px">›</div>

<!-- CONTACT FORM -->
<div class="abs form-band"></div>
<form class="abs form-card">
  <h2 class="abs form-title">CONTACT US TO DISCUSS YOUR<br>BUSINESS NEEDS</h2>
  <div class="abs field" style="left:68px;top:198px;width:292px;height:35px">Name</div>
  <div class="abs field" style="left:375px;top:198px;width:292px;height:35px">Email</div>
  <div class="abs field" style="left:68px;top:251px;width:292px;height:35px">Phone</div>
  <div class="abs field" style="left:375px;top:251px;width:292px;height:35px">Company</div>
  <div class="abs field" style="left:68px;top:303px;width:599px;height:90px">Message</div>
  <div class="abs btn submit">Submit</div>
  <svg class="abs fold" width="38" height="40" viewBox="0 0 38 40"><path d="M38 0 L0 40 L0 4Z" fill="var(--navy)"/><path d="M38 0 L0 40 L38 40Z" fill="#fff"/></svg>
</form>

<!-- CTA -->
<section class="abs cta"></section>
<div class="abs cta-photo" role="img" aria-label="Photo of a smiling man with a phone and laptop"></div>
<h2 class="abs cta-title">Contact Us To Discuss<br>Your Business Needs</h2>
<div class="abs cta-line" style="top:3566px"><svg width="20" height="20" viewBox="0 0 20 20" fill="none" stroke="#fff" stroke-width="1.5"><path d="M4 3l3 0 1.5 4-2 1.3a9 9 0 0 0 5.2 5.2L13 11.5l4 1.5v3a1.5 1.5 0 0 1-1.6 1.5A14 14 0 0 1 2.5 4.6 1.5 1.5 0 0 1 4 3z"/></svg><i></i>01 555 0147</div>
<div class="abs cta-rule"></div>
<div class="abs cta-line" style="top:3620px"><svg width="20" height="16" viewBox="0 0 20 16" fill="none" stroke="#fff" stroke-width="1.5"><rect x="1" y="1" width="18" height="14"/><path d="M1 1l9 7 9-7"/></svg><i></i>info@corvane-solutions.com</div>
<div class="abs btn-pill cta-btn">Contact Us</div>
<svg class="abs cta-curve" width="1200" height="100" viewBox="0 0 1200 100">
  <path d="M0 40 C400 80 800 75 1200 30 L1200 100 L0 100Z" fill="#0c0c0c"/>
  <path d="M0 40 C400 80 800 75 1200 30" fill="none" stroke="var(--orange)" stroke-width="4"/>
</svg>

<!-- FOOTER -->
<footer class="abs footer">
  <div class="abs f-item" style="left:163px;top:70px"><span class="f-icon"><svg width="16" height="20" viewBox="0 0 16 20" fill="none" stroke="#fff" stroke-width="1.6"><path d="M8 19s6-6 6-11A6 6 0 0 0 2 8c0 5 6 11 6 11z"/><circle cx="8" cy="8" r="2"/></svg></span><span>Northlight Studio Works<br>14 Harbour Row, Westfield,<br>Dublin 8, D08 QP21</span></div>
  <div class="abs f-sep" style="left:488px;top:80px"></div>
  <div class="abs f-item" style="left:514px;top:76px"><span class="f-icon"><svg width="16" height="12" viewBox="0 0 16 12" fill="#fff"><path d="M0 0h16v12H0z"/><path d="M0 0l8 6 8-6" stroke="#0c0c0c" stroke-width="1.4" fill="none"/></svg></span><span>Email us:<br>info@corvane-solutions.com</span></div>
  <div class="abs f-sep" style="left:808px;top:80px"></div>
  <div class="abs f-brand"><span class="dot"></span><span>CORVANE<br>SOLUTIONS</span></div>
  <p class="abs copy">© 2022 Corvanesolutions. All Rights Reserved.</p>
  <span class="abs social" style="left:966px"></span>
  <span class="abs social" style="left:1008px"></span>
</footer>

</body>
</html>
```